Church Website with Home Page and Member Sermon Library

I am in need of an updated design for our church website. This will include 4 pages (outlined below). We are a conservative, evangelical, Christian church. The site should be modern and clean, while still reflecting our conservative values. I already have a logo for our church, and I want the site to incorporate the logo, and match the logo/branding. Stock photos are allowed if needed, but I have uploaded some images of our church and would prefer those images to be used if possible. Any stock photos used should not include any people in the photos (scenery, nature, buildings, animals, etc. are fine).

The site will need 4 pages: Home, Support Us (Donate), Login, and Recording Library.

Page 1: Home
The home page should include the following sections:

- Navigation: Should include links to each section of the home page plus a "listen live" link which will take the user to a live-streaming site and a "support us" link which will take the user to a support/donate page.

- Announcements: Can be either a banner or some other design, but there needs to be some way for us to post announcements for visitors to see. I'm open for creative ideas in this section, but would like it not to take up a lot of room on the page.

- About Us: Should include address, service times (see attached document), and information about the church.

- Pastor Bio: A section that introduces our pastor and gives a short bio about our pastor. Would like this section to include a picture of our pastor. Somewhere in this section I would like to include this Bible reference: "And I will give you pastors according to mine heart, which shall feed you with knowledge and understanding. Jer 3:15 KJV"

- Articles of Faith (What We Believe): This should include several sub-sections each with a heading, body, and possibly 1 or more scripture references. I have attached a document to the brief that includes our articles of faith. Feel free to be creative with this section in how you lay these out and format them.

- Support Us: A small section that explains what kind of support someone can give and a link to a donation page. The link can say something like "Support Us" or "Donate Now".

- Contact form: A contact form that allows the visitor to send us a message. The contact form should ask for name, email, phone, and message.

- Footer: A footer that will be displayed on all pages of the site. This should include at a minimum a link to the home page (or a link to each individual section in the home page if you prefer), a link to "listen live", a link to "support us", a link to "contact us" (or you can put the contact form directly in the footer if you prefer), the address, and a "member login" link.

Page 2: Support Us
The donation page should include a form the visitor can fill out to make a donation. We will embed a third party form later. For this design, please just mock out the design with a basic form asking for name, phone, and email.

Page 3: Login
The recording library (detailed below) will require members to login with a shared numeric code before accessing the page. We need a design for a login screen. The screen should include navigation/footer just like all other pages, but the body of the login page will consist only of a form that asks the user to enter the access code and then a "login" button.

Page 4: Recording Library

The library page is a member-only page that will require a shared, numeric pass code to access. On this page, members will be able to access a filterable list of past sermons. The page by default should display most recent sermons, but should also include a search form that allows the member to filter the sermon list to find a particular sermon. The search form should allow the user to select a filter type (e.g. Speaker name, date, event, etc.) and type in a value to search. They should be able to add multiple filters and remove filters that have been added. Each sermon that is displayed in the result list should include basic information such as title, date, speaker, tags, etc. along with a download icon, and an embedded audio player where they can click a play button to stream it on-demand. Each sermon should also have clickable tags associated with it that can be used to find related sermons.
Updates

I have uploaded several images of our church. Feel free to incorporate these into your design if possible.

Target Market(s)

Church Members

Industry/Entity Type

Religion

Number of Pages Required

4 page

Font styles to use
Sans Serif

Colors

Designer to choose colors to be used in the design.

Requirements
Must have
• Must incorporate the logo (attached)
Nice to have
• Would like the design to incorporate pictures of our church (attached) instead of stock photos if possible.
Should not have
• Please avoid an overly cluttered design. Stock photos used should not include any people in the photos.

```html
<!DOCTYPE html>
<html lang="en">
<head>
<meta charset="utf-8">
<title>Cedar Grove Chapel</title>
<link href="https://fonts.googleapis.com/css2?family=Playfair+Display:ital,wght@0,400;0,700;1,400&family=Poppins:wght@300;400;500;600&display=swap" rel="stylesheet">
<style>
:root{
  --teal:#04a9c4;
  --sage:#6f8a5c;
  --ink:#2b2b2b;
  --body:#7a7a7a;
  --gold:#a9a06a;
  --light:#f2f3f1;
  --white:#fff;
}
*{margin:0;padding:0;box-sizing:border-box}
html,body{width:1200px;height:3045px;overflow:hidden}
body{position:relative;font-family:'Poppins',sans-serif;background:var(--white);color:var(--ink)}
.abs{position:absolute}
.photo{position:absolute}
.btn{position:absolute;display:flex;align-items:center;justify-content:center;gap:10px;border-radius:30px;color:var(--white);font-weight:600;font-size:13px;text-transform:uppercase;letter-spacing:.2px;text-decoration:none;border:0;font-family:'Poppins',sans-serif}
.btn svg{width:12px;height:8px}
.btn-teal{background:var(--teal)}
.btn-sage{background:var(--sage)}

/* hero */
.hero{left:0;top:0;width:1200px;height:590px;background:linear-gradient(180deg,#3b2418 0%,#5a3420 40%,#3a2214 100%)}
.hero-shade{left:0;top:0;width:1200px;height:590px;background:radial-gradient(ellipse at 50% 40%,rgba(120,70,40,.5),rgba(20,10,5,.4))}
.brand{left:0;width:1200px;text-align:center;color:var(--gold);font-family:'Playfair Display',serif;font-size:22px;letter-spacing:1px}
.brand-mark{left:578px;width:44px;height:44px;border:2px solid var(--teal);border-radius:50%}
.nav{left:0;top:158px;width:1200px;display:flex;justify-content:center;gap:34px;font-family:'Playfair Display',serif;font-size:12px;text-transform:uppercase}
.nav a{color:var(--white);text-decoration:none;padding:9px 20px;border-radius:20px}
.nav a.active{background:var(--teal)}
.hero-title{left:0;top:246px;width:1200px;text-align:center;color:var(--white);font-family:'Playfair Display',serif;font-weight:700;font-size:75px;line-height:84px}

/* service band */
.services{left:0;top:590px;width:1200px;height:84px;background:var(--teal);display:flex;align-items:center;justify-content:center;color:var(--white);font-family:'Playfair Display',serif;font-size:13px;text-transform:uppercase}
.services .day{font-size:15px;margin:0 50px 0 14px}
.services .sep{margin:0 36px}

/* about */
.kicker{color:var(--teal);font-family:'Playfair Display',serif;font-weight:700;font-size:17px;letter-spacing:5px}
.h2{font-family:'Playfair Display',serif;font-weight:700;color:var(--ink)}
.copy{font-size:11.5px;line-height:19.5px;color:var(--body);font-weight:300}
.feature{display:flex;align-items:center;gap:16px;font-family:'Playfair Display',serif;font-size:11.5px;color:var(--body);line-height:16px}

/* articles */
.articles-bg{left:0;top:1182px;width:1200px;height:820px;background:linear-gradient(180deg,#fff 0%,var(--light) 30%,var(--light) 100%)}
.rule{left:579px;top:1293px;width:42px;height:3px;background:var(--teal)}
.article-title{font-family:'Playfair Display',serif;font-weight:400;font-size:27px;color:var(--ink)}
.article-copy{font-size:10.8px;line-height:19.5px;color:var(--body);text-align:justify;font-weight:300}

/* video band */
.video-band{left:0;top:2001px;width:1200px;height:290px;background:linear-gradient(180deg,#8ba575,#6f8a5c)}
.video-title{left:0;top:2052px;width:1200px;text-align:center;color:var(--white);font-family:'Playfair Display',serif;font-weight:400;font-size:42px;line-height:48px}
.btn-outline{border:2px solid var(--white);background:transparent}

/* contact */
.contact{left:250px;top:2236px;width:700px;display:flex;gap:8px}
.contact input{height:34px;border:1px solid rgba(255,255,255,.7);background:rgba(255,255,255,.12);border-radius:17px;padding:0 14px;color:var(--white);font-family:'Poppins',sans-serif;font-size:11px;width:124px}
.contact input::placeholder{color:rgba(255,255,255,.85)}
.contact input.msg{width:200px}
.contact button{position:static;height:34px;width:96px;font-size:11px;background:var(--teal)}

/* pastor */
.placeholder{left:160px;top:2370px;width:374px;height:373px;background:#cccccc;display:flex;align-items:center;justify-content:center;color:#9a9a9a;font-size:38px}
.verse{left:0;top:2768px;width:1200px;text-align:center;font-family:'Playfair Display',serif;font-style:italic;font-size:14px;color:var(--body)}
.verse cite{font-style:normal;color:var(--teal);margin-left:8px;font-size:12px}

/* footer */
.footer{left:0;top:2827px;width:1200px;height:172px;background:linear-gradient(180deg,#3a2d27,#2b221e)}
.social{display:flex;gap:5px}
.social span{width:29px;height:29px;border:1.5px solid var(--white);border-radius:50%}
.foot-links{display:flex;gap:40px;font-size:12.5px;color:var(--white);text-transform:uppercase}
.phone{display:flex;align-items:center;gap:8px;color:var(--white);font-size:12.5px;font-weight:500}
.address{color:rgba(255,255,255,.75);font-size:11px;text-align:right;width:300px}
.copyright{left:0;top:2999px;width:1200px;height:46px;background:var(--teal);display:flex;align-items:center;justify-content:center;color:var(--white);font-size:10.5px;font-weight:500;text-transform:uppercase}
</style>
</head>
<body>

<!-- hero -->
<div class="photo hero" role="img" aria-label="Interior of a wooden church with columns and pews"></div>
<div class="abs hero-shade"></div>
<div class="abs brand-mark" style="top:28px"></div>
<div class="abs brand" style="top:90px">Cedar Grove Chapel</div>
<nav class="abs nav"><a class="active" href="#">Home</a><a href="#">Library</a><a href="#">Donation</a><a href="#">Listen Live</a></nav>
<h1 class="abs hero-title">Discover Christ<br>Find Home</h1>

<!-- service times -->
<div class="abs services">
  <svg width="50" height="50" viewBox="0 0 50 50" fill="none" stroke="#fff" stroke-width="2"><path d="M25 3v8M21 6h8"/><path d="M25 11l-9 10h18z"/><rect x="17" y="21" width="16" height="25"/><path d="M5 46V32l12-7M45 46V32l-12-7"/><path d="M22 46v-8h6v8"/><path d="M3 46h44"/></svg>
  <span class="day">Sundays</span>
  <span>8:00 AM</span><span class="sep">|</span><span>9:30 AM</span><span class="sep">|</span><span>10:30 AM</span><span class="sep">|</span><span>11:30 AM</span>
</div>

<!-- about -->
<div class="photo" style="left:161px;top:754px;width:396px;height:397px;background:linear-gradient(180deg,#e8d2a0 0%,#b98650 45%,#5a2e18 100%)" role="img" aria-label="Bright church nave with arched ceiling and rows of wooden pews"></div>
<div class="abs kicker" style="left:590px;top:772px">About Us</div>
<h2 class="abs h2" style="left:589px;top:797px;font-size:42px;line-height:47px">We Will Help You Find<br>Way to Jesus</h2>
<p class="abs copy" style="left:590px;top:906px;width:440px">Aliquam erat volutpat. Proin semper dictum pulvinar. Quisque a ligula libero. Aliquam eu nulla tortor. Nunc nec nunc quis augue porttitor efficitur. Quisque nec augue ut velit semper scelerisque quis a nisl. Aliquam erat volutpat. Proin semper dictum pulvinar.</p>
<div class="abs feature" style="left:589px;top:1004px">
  <svg width="32" height="44" viewBox="0 0 32 44" fill="none" stroke="#6f8a5c" stroke-width="1.5"><rect x="2" y="2" width="28" height="38"/><path d="M6 40v3h24"/><path d="M16 8v18M10 14h12"/></svg>
  <span>Every Sunday<br>Ceremonies</span>
</div>
<div class="abs feature" style="left:747px;top:1004px">
  <svg width="44" height="44" viewBox="0 0 50 50" fill="none" stroke="#6f8a5c" stroke-width="1.8"><path d="M25 3v8M21 6h8"/><path d="M25 11l-9 10h18z"/><rect x="17" y="21" width="16" height="25"/><path d="M5 46V32l12-7M45 46V32l-12-7"/><path d="M22 46v-8h6v8"/></svg>
  <span>Biggest Prayers<br>Community</span>
</div>
<a class="btn btn-sage" href="#" style="left:590px;top:1076px;width:130px;height:41px">Read More <svg viewBox="0 0 12 8"><path d="M0 4h10M7 1l3 3-3 3" stroke="#fff" stroke-width="1.6" fill="none"/></svg></a>

<!-- articles of faith -->
<div class="abs articles-bg"></div>
<h2 class="abs h2" style="left:0;top:1232px;width:1200px;text-align:center;font-size:44px;font-weight:400">Articles of Faith</h2>
<div class="abs rule"></div>

<div class="photo" style="left:39px;top:1343px;width:428px;height:616px;background:linear-gradient(180deg,#3f8fd6 0%,#8dbbe4 35%,#a45a3e 60%,#7b3f2c 100%)" role="img" aria-label="Red brick cathedral with towers against a blue sky"></div>
<h3 class="abs article-title" style="left:524px;top:1383px">The God Head.</h3>
<p class="abs article-copy" style="left:527px;top:1439px;width:225px">We believe in the God head bodily, known as the Divine Trinity. This body consist of God the father,Jesus Christ, his only begotten son and the rede..</p>
<a class="btn btn-teal" href="#" style="left:527px;top:1539px;width:124px;height:40px">Read More <svg viewBox="0 0 12 8"><path d="M0 4h10M7 1l3 3-3 3" stroke="#fff" stroke-width="1.6" fill="none"/></svg></a>

<div class="photo" style="left:834px;top:1340px;width:348px;height:289px;background:linear-gradient(180deg,#4a4d4a 0%,#2c2f2c 50%,#6b5f48 100%)" role="img" aria-label="Dim stone cathedral interior with lit altar"></div>
<div class="photo" style="left:483px;top:1669px;width:298px;height:290px;background:linear-gradient(135deg,#3e5a2e 0%,#a06a32 55%,#4a2a4e 100%)" role="img" aria-label="Flowers and greenery arranged on a wooden casket"></div>
<h3 class="abs article-title" style="left:853px;top:1703px">Full Salvation</h3>
<p class="abs article-copy" style="left:857px;top:1752px;width:274px">We believe that Salvation is received only when a person comes to the realization that he or she is lost and separated from God and becomes full of godly sorrow, confessing their sins and true repentance, believing in the shed blood of the Lord Jesus Christ as the only sacrifice for sins.</p>
<a class="btn btn-teal" href="#" style="left:857px;top:1891px;width:125px;height:41px">Read More <svg viewBox="0 0 12 8"><path d="M0 4h10M7 1l3 3-3 3" stroke="#fff" stroke-width="1.6" fill="none"/></svg></a>

<!-- video band with contact form -->
<div class="photo video-band" role="img" aria-label="Rows of church pews under a green tint"></div>
<h2 class="abs video-title">Watch videos of our ceremonies<br>and join our Happy family</h2>
<a class="btn btn-outline" href="#" style="left:473px;top:2180px;width:268px;height:44px">Announcements to visitors <svg viewBox="0 0 12 8"><path d="M0 4h10M7 1l3 3-3 3" stroke="#fff" stroke-width="1.6" fill="none"/></svg></a>
<form class="abs contact" style="top:2240px">
  <input type="text" placeholder="Name">
  <input type="email" placeholder="Email">
  <input type="tel" placeholder="Phone">
  <input class="msg" type="text" placeholder="Message">
  <button class="btn" type="submit">Send</button>
</form>

<!-- pastor -->
<div class="abs placeholder" role="img" aria-label="Pastor portrait">150x150</div>
<h2 class="abs h2" style="left:588px;top:2368px;font-size:42px">Pastor Bio</h2>
<div class="abs" style="left:589px;top:2420px;font-size:11px;color:var(--body);text-transform:uppercase;font-weight:300">Lorum Ipslum</div>
<p class="abs copy" style="left:589px;top:2446px;width:452px;font-size:11px;line-height:21px;text-align:justify">We believe that Salvation is received only when a person comes to the realization that he or she is lost and separated from God and becomes full of godly sorrow, confessing their sins and true repentance, believing in the shed blood of the Lord Jesus Christ as the only sacrifice for sins We believe that Salvation is received only when a person comes to the realization that he or she is lost and separated from God and becomes full of godly sorrow, confessing their sins and true repentance, believing in the shed blood of the Lord Jesus Christ as the only sacrifice for sins.</p>
<p class="abs copy" style="left:589px;top:2605px;width:452px;font-size:11px;line-height:21px;text-align:justify">We believe that Salvation is received only when a person comes to the realization that he or she is lost and separated from God and becomes full of godly sorrow, confessing their sins and true repentance, believin.</p>
<a class="btn btn-teal" href="#" style="left:590px;top:2691px;width:259px;height:41px">Live-streaming the services <svg viewBox="0 0 12 8"><path d="M0 4h10M7 1l3 3-3 3" stroke="#fff" stroke-width="1.6" fill="none"/></svg></a>
<p class="abs verse">“And I will give you pastors according to mine heart, which shall feed you with knowledge and understanding.”<cite>Jer 3:15 KJV</cite></p>

<!-- footer -->
<footer class="photo footer" role="img" aria-label="Darkened church interior behind the footer"></footer>
<div class="abs social" style="left:160px;top:2891px" aria-label="Social links"><span></span><span></span><span></span></div>
<div class="abs foot-links" style="left:161px;top:2935px"><span>Home</span><span>Library</span><span>Donation</span><span>Listen Live</span></div>
<div class="abs brand-mark" style="top:2857px"></div>
<div class="abs brand" style="top:2920px">Cedar Grove Chapel</div>
<a class="btn btn-sage" href="#" style="left:901px;top:2884px;width:137px;height:39px">Donate Now <svg viewBox="0 0 12 8"><path d="M0 4h10M7 1l3 3-3 3" stroke="#fff" stroke-width="1.6" fill="none"/></svg></a>
<div class="abs phone" style="left:870px;top:2934px">
  <svg width="12" height="12" viewBox="0 0 24 24" fill="#fff"><path d="M6.6 10.8a15.2 15.2 0 006.6 6.6l2.2-2.2a1 1 0 011-.25 11.4 11.4 0 003.6.57 1 1 0 011 1V20a1 1 0 01-1 1A17 17 0 013 4a1 1 0 011-1h3.5a1 1 0 011 1c0 1.25.2 2.45.57 3.57a1 1 0 01-.25 1z"/></svg>
  <span>Phone : + 10 555 014 27</span>
</div>
<div class="abs address" style="left:738px;top:2960px">214 Cedar Grove Road, Millbrook</div>
<div class="abs copyright">Copyright ©2023 Cedar Grove Chapel | All right reserved.</div>

</body>
</html>
```